Korvel Staffing Full Length Retractable Office Banner

I need a design for a full-length retractable banner and A-Frame Sign for each of my offices. I have included designs that have been incorporated into a poster and tri-fold as a sample. I would like to see a colorful eyecatching banner that focuses on people. Would like to see some diversity with men and woman and different races.
Korvel Staffing is a light industrial staffing firm. www.KorvelStaffing.example

Target Market(s)

Job seekers looking for employment

Industry/Entity Type

Staffing / Recruiting

Font styles to use
Other font styles liked:
• Professional yet fun

Requirements
Must have
• Eye catching design with young hip vibe.
Nice to have
• primary colors with light industrial type jobs

```html
<!DOCTYPE html>
<html lang="en">
<head>
<meta charset="utf-8">
<title>Korvel Staffing – Retractable Banner</title>
<link rel="stylesheet" href="https://fonts.googleapis.com/css2?family=Bebas+Neue&display=swap">
<style>
  :root {
    --page-bg: #eeeeef;
    --banner-bg: #ffffff;
    --navy: #27255f;
    --red: #e2332a;
    --green: #14803f;
    --yellow: #e8c21a;
    --photo-warm: #d9a164;
    --photo-tan: #c79a7c;
    --photo-dark: #2c2a2e;
    --photo-olive: #6d6a3a;
  }
  * { margin: 0; padding: 0; box-sizing: border-box; }
  html, body {
    width: 1200px;
    height: 2434px;
    overflow: hidden;
    background: var(--page-bg);
  }
  .banner {
    position: absolute;
    left: 112px;
    top: 67px;
    width: 976px;
    height: 2300px;
    background: var(--banner-bg);
    box-shadow: 6px 8px 18px rgba(0,0,0,0.18);
    font-family: "Bebas Neue", "Oswald", sans-serif;
    color: var(--navy);
  }
  .brand-name {
    position: absolute;
    top: 170px;
    left: 0;
    width: 100%;
    text-align: center;
    font-size: 170px;
    line-height: 1;
    letter-spacing: 6px;
    color: var(--navy);
  }
  .team-photo {
    position: absolute;
    left: 0;
    top: 0;
    width: 976px;
    height: 2300px;
  }
  .tagline {
    position: absolute;
    left: 62px;
    top: 1452px;
    font-size: 98px;
    line-height: 116px;
    letter-spacing: 7px;
  }
  .color-rule {
    position: absolute;
    left: 0;
    top: 1906px;
    width: 100%;
    height: 12px;
    display: flex;
  }
  .color-rule span { flex: 1; }
  .color-rule .red { background: var(--red); }
  .color-rule .green { background: var(--green); }
  .color-rule .yellow { background: var(--yellow); }
  .color-rule .navy { background: var(--navy); }
  .web-address {
    position: absolute;
    top: 2050px;
    left: 0;
    width: 100%;
    text-align: center;
    font-size: 66px;
    letter-spacing: 12px;
  }
</style>
</head>
<body>
  <main class="banner">
    <div class="brand-name">Korvel Staffing</div>

    <svg class="team-photo" viewBox="0 0 976 2300" role="img" aria-label="Photo of four smiling young adults of diverse backgrounds in winter jackets standing together">
      <defs>
        <clipPath id="photo-shape">
          <circle cx="488" cy="790" r="560"/>
        </clipPath>
        <linearGradient id="photo-tones" x1="0" y1="0" x2="1" y2="0">
          <stop offset="0" stop-color="var(--photo-warm)"/>
          <stop offset="0.35" stop-color="var(--photo-tan)"/>
          <stop offset="0.6" stop-color="var(--photo-dark)"/>
          <stop offset="0.8" stop-color="#8a3a24"/>
          <stop offset="1" stop-color="var(--photo-olive)"/>
        </linearGradient>
      </defs>
      <rect x="0" y="576" width="976" height="780" fill="url(#photo-tones)" clip-path="url(#photo-shape)"/>
    </svg>

    <h1 class="tagline">Connecting<br>Great People With<br>Great Organizations</h1>

    <div class="color-rule">
      <span class="red"></span><span class="green"></span><span class="yellow"></span><span class="navy"></span>
    </div>

    <p class="web-address">www.KorvelStaffing.example</p>
  </main>
</body>
</html>
```